Astrology Reading Website to attract clients

I need a website for my astrology practice. My business name is Velvet Harbor Astrology. I will need a page the following pages: About, Readings, Booking, Contact, and Blog. I will need full figma or figma-like mockups of pages along with assets. I will need both desktop and mobile designs.
I like creams, dark blues and greens. I am fine with planets or other astrology symbolism.

Target Market(s)

new age, spiritual

Industry/Entity Type

Holistic, spiritual

Number of Pages Required

3 page

Colors
0054AA
0677BA
7BADD7
CADEEF
E8F1F8

Requirements
Nice to have
• calm and grounded backgrounds

```html
<!DOCTYPE html>
<html lang="en">
<head>
<meta charset="utf-8">
<title>Velvet Harbor Astrology</title>
<link href="https://fonts.googleapis.com/css2?family=Jost:wght@400;500;600;700&display=swap" rel="stylesheet">
<style>
:root{
  --blue:#0054aa;
  --blue-mid:#0677ba;
  --blue-soft:#7badd7;
  --blue-pale:#cadeef;
  --ice:#e8f1f8;
  --ink:#111111;
  --text:#222222;
  --muted:#555555;
  --white:#ffffff;
  --grey-bg:#f1f1f2;
  --night:#0e0c24;
}
*{box-sizing:border-box;margin:0;padding:0}
html,body{width:1200px;height:3601px;overflow:hidden}
body{position:relative;font-family:"Jost",sans-serif;color:var(--text);background:var(--white)}
.abs{position:absolute}
.btn{position:absolute;display:flex;align-items:center;justify-content:center;background:var(--blue);color:var(--white);font-weight:600;font-size:15px;text-decoration:none}

/* Hero */
.hero{position:absolute;left:0;top:0;width:1200px;height:617px;
  background:radial-gradient(ellipse at 70% 60%,#4a3a8a 0%,rgba(40,30,90,.6) 35%,transparent 65%),
             radial-gradient(ellipse at 20% 30%,#2b2f6e 0%,transparent 55%),
             linear-gradient(180deg,#121033 0%,#1b1748 55%,#2a2262 100%)}
.brand{position:absolute;left:63px;top:28px;display:flex;align-items:center;gap:14px}
.brand-dot{width:67px;height:67px;border-radius:50%;background:var(--blue)}
.brand-name{color:var(--white);font-weight:600;font-size:22px}
.nav{position:absolute;left:514px;top:50px;display:flex;gap:25px}
.nav a{color:var(--white);font-weight:500;font-size:16px;text-decoration:none}
.hero-title{position:absolute;left:0;width:1200px;top:268px;text-align:center;color:var(--white);font-weight:600;font-size:36px}
.hero-sub{position:absolute;left:0;width:1200px;top:332px;text-align:center;color:var(--white);font-weight:500;font-size:19px}

/* About */
.about-title{left:63px;top:690px;font-size:36px;font-weight:700;color:var(--blue)}
.about-text{left:63px;top:760px;width:462px;font-size:13.3px;line-height:18.2px;color:var(--ink)}
.about-text p+p{margin-top:18px}
.about-img{left:617px;top:691px;width:521px;height:347px;
  background:radial-gradient(circle at 50% 52%,#f6d48a 0%,#b87a2a 12%,#4a2c14 32%,#150f0c 60%,#050507 100%)}

/* Readings */
.readings{left:0;top:1112px;width:1200px;height:689px;
  background:radial-gradient(ellipse at 55% 45%,#3a3324 0%,#1d1a16 45%,#0c0b0a 100%)}
.section-title-light{left:0;width:1200px;top:1154px;text-align:center;color:var(--white);font-size:33px;font-weight:700}
.book{top:1256px;width:341px;height:449px}
.book .cover{width:331px;height:439px}
.book.blue{background:var(--blue)}
.book.white{background:var(--white)}
.cover-moon{background:radial-gradient(circle at 52% 62%,#b8b25a 0%,#6f6c2c 28%,#24301f 55%,#122028 100%)}
.cover-wheel{background:radial-gradient(circle at 50% 64%,#e0822a 0%,#8a2c12 30%,#1a0a06 52%,#000 70%)}
.cover-nebula{background:radial-gradient(circle at 40% 40%,#e77aa0 0%,#8a3a8a 30%,#3a2a7a 60%,#24205a 100%)}
.dots{left:598px;top:1741px;display:flex;gap:7px}
.dots span{width:8px;height:8px;border-radius:50%;background:var(--white)}
.dots span.on{background:var(--blue-mid)}

/* Contact */
.contact{left:0;top:1801px;width:1200px;height:542px;background:var(--grey-bg)}
.contact-title{left:0;width:1200px;top:1856px;text-align:center;font-size:35px;font-weight:700;color:var(--blue)}
.contact-sub{left:0;width:1200px;top:1914px;text-align:center;font-size:17px;line-height:17px;font-weight:500;color:var(--blue)}
.field{position:absolute;background:var(--white);border:1px solid #e6e6e6;font-family:Arial,sans-serif;font-size:12px;color:#9a9a9a;padding:11px 15px}
.book-now{left:331px;top:2239px;width:536px;height:42px}

/* Promo */
.promo{left:0;top:2343px;width:1200px;height:251px;
  background:radial-gradient(ellipse at 62% 45%,#5a3f9a 0%,#2c2470 35%,#15154a 70%,#0e1040 100%)}
.promo-circle{left:52px;top:2392px;width:154px;height:154px;border-radius:50%;background:var(--blue)}
.promo-text{left:250px;width:700px;top:2420px;text-align:center;color:var(--white);font-size:35px;font-weight:700;line-height:50px}
.promo-btn{left:1000px;top:2450px;width:137px;height:37px;background:var(--white);color:var(--blue)}

/* Blogs */
.blogs-title{left:0;width:1200px;top:2652px;text-align:center;font-size:35px;font-weight:700;color:var(--blue)}
.arrow{position:absolute;top:2660px;width:31px;height:31px;border:1px solid #333;border-radius:50%;display:flex;align-items:center;justify-content:center}
.post{position:absolute;top:2734px;width:345px}
.post-img{width:345px;height:212px}
.img-galaxy{background:radial-gradient(ellipse at 50% 50%,#f6e3b8 0%,#a07a52 12%,#2b3a5a 38%,#0a0f1c 75%)}
.img-sun{background:radial-gradient(circle at 40% 48%,#fff0a0 0%,#ff9a1a 20%,#c23a05 32%,#1a0602 48%,#030100 80%)}
.img-wheel{background:radial-gradient(circle at 50% 45%,#6a6ad0 0%,#3b2f8a 35%,#2a1a5a 65%,#7a3a6a 90%,#b05a5a 100%)}
.post-meta{display:flex;justify-content:space-between;width:312px;margin-top:25px;font-size:11px;color:var(--blue-mid)}
.post-title{margin-top:20px;font-size:16px;font-weight:600;color:var(--ink)}
.post-text{margin-top:14px;width:290px;font-size:12.5px;line-height:18px;color:var(--muted)}
.post .btn{position:relative;margin-top:23px;width:137px;height:37px}

/* Footer */
.footer{left:0;top:3227px;width:1200px;height:374px;background:#000}
.foot-circle{left:63px;top:3279px;width:106px;height:106px;border-radius:50%;background:var(--white)}
.foot-name{left:190px;top:3316px;color:var(--white);font-size:22px;font-weight:600}
.foot-text{left:66px;top:3403px;width:370px;color:var(--white);font-size:13.5px;line-height:21px}
.foot-head{color:var(--blue-mid);font-size:16px;font-weight:500}
.support-item{position:absolute;left:610px;display:flex;align-items:center;gap:18px;color:var(--white);font-size:14px;line-height:17px}
.icon-dot{width:38px;height:38px;border-radius:50%;background:var(--white);display:flex;align-items:center;justify-content:center;flex:none}
.quick{left:1048px;top:3275px}
.quick ul{margin-top:13px;list-style:none}
.quick li{color:var(--white);font-size:14px;line-height:30px}
.quick li::before{content:"•";margin:0 8px 0 8px}
.foot-rule{left:0;top:3543px;width:1200px;height:1px;background:#3a3a3a}
.copyright{left:0;width:1200px;top:3564px;text-align:center;color:var(--white);font-size:13px}
</style>
</head>
<body>

<header class="hero" role="img" aria-label="Starry night sky with a constellation"></header>
<div class="brand"><span class="brand-dot"></span><span class="brand-name">Velvet Harbor Astrology</span></div>
<nav class="nav"><a href="#">Home</a><a href="#">About</a><a href="#">Readings</a><a href="#">Booking</a><a href="#">Blogs</a></nav>
<a class="btn" href="#" style="left:1028px;top:43px;width:109px;height:38px">Contact</a>
<h1 class="hero-title">Discover Your Destiny with Velvet Harbor Astrology</h1>
<p class="hero-sub">Unveil the secrets of the universe and gain insights into your life.</p>
<a class="btn" href="#" style="left:530px;top:378px;width:140px;height:37px">Learn more</a>

<h2 class="abs about-title">About</h2>
<div class="abs about-text">
  <p>Lorem ipsum dolor sit amet, consectetuer adipiscing elit, sed diam nonummy nibh euismod tincidunt ut laoreet dolore magna aliquam erat volutpat. Ut wisi enim ad minim veniam, quis nostrud exerci tation ullamcorper suscipit lobortis nisl ut aliquip ex ea commodo consequat. Duis autem vel eum iriure dolor in hendrerit in vulputate velit esse molestie consequat, vel illum dolore eu feugiat nulla facilisis at vero eros et accumsan et iusto odio dignissim qui blandit praesent luptatum zzril delenit augue duis dolore te feugait nulla facilisi.</p>
  <p>&nbsp;dolore eu feugiat nulla facilisis at vero eros et accumsan et iusto odio dignissim qui blandit praesent luptatum zzril delenit augue duis dolore te feugait nulla facilisi.</p>
</div>
<a class="btn" href="#" style="left:63px;top:1000px;width:140px;height:38px">Learn more</a>
<div class="abs about-img" role="img" aria-label="Golden zodiac wheel glowing in a starfield"></div>

<section class="abs readings" role="img" aria-label="Dim backdrop of a zodiac chart"></section>
<h2 class="abs section-title-light">Readings</h2>
<div class="abs book blue" style="left:63px"><div class="cover cover-moon" role="img" aria-label="Book cover with a golden moon"></div></div>
<div class="abs book white" style="left:431px"><div class="cover cover-wheel" role="img" aria-label="Book cover with a zodiac wheel around a human figure"></div></div>
<div class="abs book white" style="left:799px"><div class="cover cover-nebula" role="img" aria-label="Book cover with a pink nebula"></div></div>
<div class="abs dots"><span class="on"></span><span></span><span></span></div>

<section class="abs contact"></section>
<h2 class="abs contact-title">Contact</h2>
<p class="abs contact-sub">Ready to embark on your astrological Journey?<br>Book your appointment today</p>
<div class="field" style="left:331px;top:1990px;width:261px;height:35px">Your Name</div>
<div class="field" style="left:604px;top:1990px;width:262px;height:35px">E - Mail</div>
<div class="field" style="left:331px;top:2042px;width:261px;height:35px">Date and Time</div>
<div class="field" style="left:604px;top:2042px;width:262px;height:35px">Date of Birth</div>
<div class="field" style="left:332px;top:2101px;width:535px;height:116px;padding-top:13px">Message...</div>
<a class="btn book-now" href="#">Book Now</a>

<section class="abs promo" role="img" aria-label="Purple galaxy sky"></section>
<div class="abs promo-circle"></div>
<p class="abs promo-text">Unlock the Secrets of Your Future!<br>50% Off Your First Astrology Reading!</p>
<a class="btn promo-btn" href="#">Book Now</a>

<h2 class="abs blogs-title">Blogs</h2>
<span class="arrow" style="left:1068px"><svg width="10" height="10" viewBox="0 0 10 10"><path d="M6.5 1.5 3 5l3.5 3.5" fill="none" stroke="#222" stroke-width="1.6"/></svg></span>
<span class="arrow" style="left:1106px"><svg width="10" height="10" viewBox="0 0 10 10"><path d="M3.5 1.5 7 5 3.5 8.5" fill="none" stroke="#222" stroke-width="1.6"/></svg></span>

<article class="post" style="left:63px">
  <div class="post-img img-galaxy" role="img" aria-label="Spiral galaxy in deep space"></div>
  <div class="post-meta"><span>11 Mar 2024</span><span>Read 7 Mins</span></div>
  <h3 class="post-title" style="margin-top:26px">Monthly Horoscopes</h3>
  <p class="post-text">Lorem ipsum dolor sit amet, consectetuer adipiscing elit, sed diam nonummy nibh euismod tincidunt</p>
  <a class="btn" href="#">Read more</a>
</article>
<article class="post" style="left:428px">
  <div class="post-img img-sun" role="img" aria-label="Glowing sun beside a crescent planet"></div>
  <div class="post-meta"><span>23 Jan 2017</span><span>Read 7 Mins</span></div>
  <h3 class="post-title">Planetary Transits</h3>
  <p class="post-text" style="margin-top:20px">Lorem ipsum dolor sit amet, consectetuer adipiscing elit, sed diam nonummy nibh euismod tincidunt</p>
  <a class="btn" href="#">Read more</a>
</article>
<article class="post" style="left:792px">
  <div class="post-img img-wheel" role="img" aria-label="Zodiac wheel over a dusk horizon"></div>
  <div class="post-meta"><span>30 Mar 2020</span><span>Read 7 Mins</span></div>
  <h3 class="post-title">Astrological Tips for Daily Life</h3>
  <p class="post-text" style="margin-top:20px">Lorem ipsum dolor sit amet, consectetuer adipiscing elit, sed diam nonummy nibh euismod tincidunt</p>
  <a class="btn" href="#">Read more</a>
</article>

<footer class="abs footer"></footer>
<div class="abs foot-circle"></div>
<div class="abs foot-name">Velvet Harbor Astrology</div>
<p class="abs foot-text">Lorem ipsum dolor sit amet, consectetuer adipiscing elit, sed diam nonummy nibh euismod tincidunt ut laoreet dolore magna aliquam erat</p>

<div class="abs foot-head" style="left:610px;top:3279px">Customer Support</div>
<div class="support-item" style="top:3319px">
  <span class="icon-dot"><svg width="16" height="16" viewBox="0 0 24 24"><path d="M6.6 10.8a15 15 0 0 0 6.6 6.6l2.2-2.2c.3-.3.7-.4 1-.2 1.1.4 2.3.6 3.6.6.6 0 1 .4 1 1V20c0 .6-.4 1-1 1A17 17 0 0 1 3 4c0-.6.4-1 1-1h3.5c.6 0 1 .4 1 1 0 1.3.2 2.5.6 3.6.1.3 0 .7-.2 1z" fill="#0054aa"/></svg></span>0123456789
</div>
<div class="support-item" style="top:3387px">
  <span class="icon-dot"><svg width="16" height="16" viewBox="0 0 24 24"><path d="M12 2a7 7 0 0 0-7 7c0 5 7 13 7 13s7-8 7-13a7 7 0 0 0-7-7zm0 9.5A2.5 2.5 0 1 1 12 6.5a2.5 2.5 0 0 1 0 5z" fill="#0054aa"/></svg></span>123,Lorem ipsum dolor sit ame,<br>nonummy nibh euismod, 1234.
</div>
<div class="support-item" style="top:3453px">
  <span class="icon-dot"><svg width="18" height="18" viewBox="0 0 24 24" fill="none" stroke="#0054aa" stroke-width="1.8"><circle cx="12" cy="12" r="9"/><path d="M3 12h18M12 3c3 3 3 15 0 18M12 3c-3 3-3 15 0 18"/></svg></span>www.velvetharborastrology.com
</div>

<div class="abs quick">
  <div class="foot-head">Quick Links</div>
  <ul><li>Home</li><li>About</li><li>Readings</li><li>Bookings</li><li>Blogs</li><li>Contact</li></ul>
</div>

<div class="abs foot-rule"></div>
<p class="abs copyright">© Copyright 2024. All Rights Reserved.</p>

</body>
</html>
```